Web interface for PC desktop app

We need an HTML design for our new PC software.

To get an idea of the project scope, please review the interface draft in the attached files. The screenshot shows almost all dialogs of our product.

Our product is software that allows users to replace static Windows wallpaper with live animated scenes. The program interface consists of a gallery where users can select and download animated scenes, as well as an information area with scene details and current desktop settings. The product will be distributed on the Vorlo platform among the gamer community.

For this project, you need to create an engaging and user-friendly interface using HTML and CSS in two color schemes (black and white). Additionally, you will need to create a colorized version of the main program icon in vector format (a draft of the program icon is attached), design all other program icons, including icons for the title bar, and redraw all other images according to your design style.

Project Requirements:
-Develop a comprehensive design for the application, including icons and images, in two color schemes: dark and light.
-Colorize our main program icon according to your design style.
-Create other UI icons in all sizes from 16x16 to 512x512 pixels, ensuring that other images are suitable for up to 4K monitors.
-Ensure all UI controls have styles for standard Windows states: normal, hovered, active, and disabled.

Deliverables:
-Final design in HTML and CSS format.
-Icons in ICO format.
-Images in PNG format.

• all interface elements, including the program title bar, coded in HTML and CSS.

```html
<!DOCTYPE html>
<html lang="en">
<head>
<meta charset="utf-8">
<title>Vivid Scene studio</title>
<link href="https://fonts.googleapis.com/css2?family=Roboto:wght@400;500;700&display=swap" rel="stylesheet">
<style>
:root{
  --blue:#2d55b2;
  --blue-soft:#3f67c4;
  --blue-inner:#4a70c9;
  --ink:#1f2329;
  --muted:#5d6470;
  --line:#d8dbe0;
  --panel:#f3f4f6;
  --field:#eceef1;
  --white:#ffffff;
  --dark:#1c1f26;
  --red:#e02a2a;
}
*{box-sizing:border-box;margin:0;padding:0}
html,body{width:1200px;height:807px;overflow:hidden}
body{font-family:"Roboto",sans-serif;color:var(--ink);background:var(--panel);position:relative}
.abs{position:absolute}

/* title bar */
.titlebar{left:0;top:0;width:1200px;height:31px;background:var(--panel)}
.app-mark{left:21px;top:5px;width:21px;height:21px;border-radius:4px;background:var(--blue)}
.app-title{left:48px;top:7px;font-size:13px}
.win-btn{top:5px;width:19px;height:19px;background:#e4e6ea;border-radius:2px;display:flex;align-items:center;justify-content:center}
.win-close{left:1143px;top:4px;width:32px;height:20px;background:var(--red);border-radius:2px;display:flex;align-items:center;justify-content:center}

/* left column */
.side-tab{top:44px;height:29px;display:flex;align-items:center;gap:6px;font-size:13px;font-weight:500}
.side-tab.active{left:24px;width:112px;background:var(--blue);color:var(--white);padding-left:15px}
.side-tab.idle{left:148px;color:var(--muted)}
.display-box{left:24px;top:73px;width:312px;height:225px;background:var(--blue)}
.display-inner{left:32px;top:85px;width:296px;height:201px;background:var(--blue-inner)}
.mon-active{left:32px;top:85px;width:157px;height:106px;background:var(--blue-soft)}
.screen{border:3px solid #111;border-radius:2px}
.stand{background:#111}
.display-meta{left:39px;top:205px;color:var(--white);font-size:12px;line-height:16px}
.display-meta b{font-weight:700}
.dark-btn{top:247px;height:29px;background:var(--dark);color:var(--white);font-size:12.5px;font-weight:500;display:flex;align-items:center;justify-content:center;gap:5px}

.scene-name{left:24px;top:319px;font-size:12.5px}
.scene-name b{font-weight:700}
.scene-preview{left:24px;top:342px;width:312px;height:199px;background:linear-gradient(160deg,#cfdbe6 0%,#93a8bb 45%,#55624f 75%,#7e8a86 100%)}
.act-btn{top:549px;height:30px;font-size:13px;font-weight:500;display:flex;align-items:center;justify-content:center;gap:6px}
.act-apply{left:24px;width:98px;background:var(--blue);color:var(--white)}
.act-test{left:129px;width:99px;background:#e6e8eb;color:var(--ink)}
.act-uninstall{left:236px;width:100px;background:#e6e8eb;color:var(--ink)}
.info-row{left:32px;width:298px;height:16px;display:flex;align-items:flex-end;font-size:12px;color:var(--muted)}
.info-row .lab{font-weight:500}
.info-row .dots{flex:1;border-bottom:1px dotted #b9bdc4;margin:0 4px 3px}
.info-row .val{width:88px;flex:none}
.stars{color:#f3a019;font-size:11px;letter-spacing:-1px}
.thumb{width:16px;height:16px;border-radius:2px;display:inline-flex;align-items:center;justify-content:center;margin-left:3px}
.create-btn{left:24px;top:709px;width:312px;height:29px;background:var(--blue);color:var(--white);font-size:13px;font-weight:500;display:flex;align-items:center;justify-content:center;gap:6px}

/* right column */
.main{left:361px;top:31px;width:839px;height:776px;background:var(--white)}
.main-tab{top:39px;height:34px;display:flex;align-items:center;gap:5px;font-size:13px;font-weight:500}
.main-tab.active{left:387px;width:102px;background:var(--blue);color:var(--white);justify-content:center}
.main-tab.idle{left:506px;color:var(--muted)}
.tab-rule{left:387px;top:72px;width:789px;height:1px;background:var(--line)}
.icon-btn{top:39px;width:26px;height:26px;background:#eceef1;display:flex;align-items:center;justify-content:center;font-size:12px;font-weight:700}
.field{top:81px;height:30px;background:var(--field);display:flex;align-items:center;justify-content:space-between;padding:0 13px;font-size:12.5px;color:#8a9099}
.card{width:388px;height:262px;overflow:hidden}
.card-empty{background:#eceef1}
.card-label{position:absolute;left:23px;bottom:21px;color:var(--white);font-size:12.5px;font-weight:500}
.dl{position:absolute;right:23px;bottom:19px;width:21px;height:21px;background:var(--blue);border-radius:2px;display:flex;align-items:center;justify-content:center}
.scroll-thumb{left:1184px;top:86px;width:6px;height:68px;background:var(--blue);border-radius:3px}

/* bottom bar */
.footer{left:361px;top:767px;width:839px;height:40px;background:var(--white)}
.foot-gray{left:387px;top:767px;width:175px;height:40px;background:#eceef1}
.pg{top:775px;height:23px;display:flex;align-items:center;justify-content:center;font-size:12.5px;font-weight:500}
.pg-prev{left:882px;width:73px;background:#eceef1}
.pg-cur{left:994px;width:22px;background:var(--blue);color:var(--white)}
.pg-next{left:1109px;width:73px;background:var(--blue);color:var(--white)}
</style>
</head>
<body>

<!-- title bar -->
<div class="abs titlebar"></div>
<div class="abs app-mark"></div>
<div class="abs app-title">Vivid Scene studio</div>
<div class="abs win-btn" style="left:1096px"><svg width="9" height="9"><line x1="0" y1="5" x2="9" y2="5" stroke="#333" stroke-width="1.2"/></svg></div>
<div class="abs win-btn" style="left:1119px"><svg width="10" height="10" fill="none" stroke="#333" stroke-width="1.2"><path d="M0 3V0h3M7 0h3v3M10 7v3H7M3 10H0V7"/></svg></div>
<div class="abs win-close"><svg width="10" height="10" stroke="#fff" stroke-width="1.8"><line x1="0" y1="0" x2="10" y2="10"/><line x1="10" y1="0" x2="0" y2="10"/></svg></div>

<!-- left column -->
<div class="abs side-tab active"><svg width="14" height="13" fill="none" stroke="#fff" stroke-width="1.3"><rect x=".7" y=".7" width="12.6" height="11.6"/><path d="M1 11l4-4 3 3 2-2 3 3"/></svg>Wallpaper</div>
<div class="abs side-tab idle"><svg width="22" height="13" fill="none" stroke="#8a9099" stroke-width="1.1"><rect x=".6" y=".6" width="20.8" height="11.8"/><path d="M2 10l5-5 4 4 3-2 5 3"/></svg>Screensavers</div>

<div class="abs display-box"></div>
<div class="abs display-inner"></div>
<div class="abs mon-active"></div>
<div class="abs screen" role="img" aria-label="Desert canyon arch wallpaper on the main display" style="left:43px;top:92px;width:133px;height:84px;background:linear-gradient(135deg,#4a3a38,#c46a2c 50%,#2b2a3b)"></div>
<div class="abs stand" style="left:107px;top:176px;width:4px;height:6px"></div>
<div class="abs stand" style="left:92px;top:182px;width:52px;height:3px;border-radius:2px"></div>
<div class="abs screen" role="img" aria-label="Mountain lake and forest wallpaper on the second display" style="left:197px;top:97px;width:123px;height:74px;background:linear-gradient(135deg,#8aa7a4,#3e6b78 50%,#3d5a2b)"></div>
<div class="abs stand" style="left:256px;top:171px;width:4px;height:6px"></div>
<div class="abs stand" style="left:236px;top:177px;width:45px;height:3px;border-radius:2px"></div>
<div class="abs display-meta"><b>Dispaly:</b> Norvik N2420HD<br><b>Wallpaper:</b> System Default</div>
<div class="abs dark-btn" style="left:39px;width:92px"><svg width="12" height="12" fill="none" stroke="#fff" stroke-width="1.2"><circle cx="6" cy="6" r="2"/><circle cx="6" cy="6" r="5" stroke-dasharray="2 1.2"/></svg>Settings</div>
<div class="abs dark-btn" style="left:137px;width:68px"><svg width="7" height="11" fill="none" stroke="#fff" stroke-width="1.5"><path d="M1 1l5 4.5L1 10"/></svg>Next</div>
<div class="abs dark-btn" style="left:211px;width:81px"><svg width="16" height="12" fill="none" stroke="#fff" stroke-width="1.2"><rect x=".6" y=".6" width="14.8" height="9"/><line x1="5" y1="11.4" x2="11" y2="11.4"/></svg>View</div>
<div class="abs dark-btn" style="left:298px;width:23px"><svg width="4" height="14" fill="#fff"><circle cx="2" cy="2" r="1.6"/><circle cx="2" cy="7" r="1.6"/><circle cx="2" cy="12" r="1.6"/></svg></div>

<div class="abs scene-name">Name: <b>Shadow Order</b></div>
<div class="abs scene-preview" role="img" aria-label="Alpine lakeside village beneath snowy mountains"></div>
<div class="abs act-btn act-apply"><svg width="11" height="13" fill="none" stroke="#fff" stroke-width="1.1"><path d="M3 7V2a1 1 0 0 1 2 0v4l5 1v3l-2 2H5L1 8l1-1 1 1"/></svg>Apply</div>
<div class="abs act-btn act-test"><svg width="14" height="11" fill="none" stroke="#777" stroke-width="1"><rect x=".5" y=".5" width="13" height="8"/><path d="M3 6l3-3 2 2 3-3"/></svg>Test</div>
<div class="abs act-btn act-uninstall"><svg width="10" height="12" fill="none" stroke="#777" stroke-width="1"><path d="M1 2.5h8M3.5 2.5V1h3v1.5M2 2.5l.6 9h4.8l.6-9"/></svg>Uninstall</div>

<div class="abs info-row" style="top:599px"><span class="lab">Autor:</span><span class="dots"></span><span class="val">CanvasWorks</span></div>
<div class="abs info-row" style="top:624px"><span class="lab">Resolution:</span><span class="dots"></span><span class="val">3840x2400</span></div>
<div class="abs info-row" style="top:649px"><span class="lab">Size:</span><span class="dots"></span><span class="val">#NAN Mb</span></div>
<div class="abs info-row" style="top:674px"><span class="lab">Rating:</span><span class="dots"></span><span class="stars">★★★★★</span><span class="thumb" style="background:#2f9bf0"><svg width="9" height="9" fill="#fff"><path d="M0 4h2v5H0zM3 4l2-4h1v3h3l-1 6H3z"/></svg></span><span class="thumb" style="background:#e6383a"><svg width="9" height="9" fill="#fff"><path d="M0 0h2v5H0zM3 5l2 4h1V6h3L8 0H3z"/></svg></span></div>

<div class="abs create-btn"><svg width="13" height="12" fill="none" stroke="#fff" stroke-width="1.1"><rect x=".5" y=".5" width="12" height="11"/><path d="M1 10l4-4 3 3 2-2 2 2"/></svg>Create Your Own Wallpaper</div>

<!-- right column -->
<div class="abs main"></div>
<div class="abs main-tab active"><svg width="14" height="13" fill="none" stroke="#fff" stroke-width="1.2"><rect x=".6" y=".6" width="12.8" height="8.5"/><path d="M7 2v5M5 5l2 2 2-2M4 12h6"/></svg>Installed</div>
<div class="abs main-tab idle"><svg width="14" height="14" fill="none" stroke="#8a9099" stroke-width="1.1"><circle cx="7" cy="7" r="6.2"/></svg>Workshop LWM1</div>
<div class="abs tab-rule"></div>
<div class="abs icon-btn" style="left:1117px"><svg width="12" height="12" fill="none" stroke="#333" stroke-width="1"><circle cx="6" cy="6" r="2"/><circle cx="6" cy="6" r="5" stroke-dasharray="2 1.2"/></svg></div>
<div class="abs icon-btn" style="left:1147px">!</div>

<div class="abs field" style="left:387px;width:258px">Search wallpaper...<svg width="11" height="11" fill="none" stroke="#8a9099" stroke-width="1.2"><circle cx="4.5" cy="4.5" r="3.8"/><line x1="7.3" y1="7.3" x2="10.5" y2="10.5"/></svg></div>
<div class="abs field" style="left:651px;width:258px"><span></span><svg width="8" height="5" fill="none" stroke="#8a9099" stroke-width="1.1"><path d="M.5.5l3.5 3.5L7.5.5"/></svg></div>
<div class="abs field" style="left:916px;width:258px">All<svg width="8" height="5" fill="none" stroke="#8a9099" stroke-width="1.1"><path d="M.5.5l3.5 3.5L7.5.5"/></svg></div>

<div class="abs card card-empty" style="left:387px;top:125px">
  <svg width="388" height="262" viewBox="0 0 388 262">
    <rect x="93" y="45" width="194" height="126" rx="6" fill="none" stroke="#8f9094" stroke-width="12"/>
    <rect x="173" y="171" width="34" height="24" fill="#8f9094"/>
    <rect x="90" y="195" width="208" height="15" rx="4" fill="#8f9094"/>
    <circle cx="190" cy="183" r="6" fill="#eceef1"/>
    <g stroke="#8f9094" stroke-width="3.5" stroke-linecap="round" transform="translate(190 111)">
      <line x1="0" y1="-22" x2="0" y2="-35" transform="rotate(0)"/>
      <line x1="0" y1="-22" x2="0" y2="-35" transform="rotate(30)"/>
      <line x1="0" y1="-22" x2="0" y2="-35" transform="rotate(60)"/>
      <line x1="0" y1="-22" x2="0" y2="-35" transform="rotate(90)"/>
      <line x1="0" y1="-22" x2="0" y2="-35" transform="rotate(120)"/>
      <line x1="0" y1="-22" x2="0" y2="-35" transform="rotate(150)"/>
      <line x1="0" y1="-22" x2="0" y2="-35" transform="rotate(180)"/>
      <line x1="0" y1="-22" x2="0" y2="-35" transform="rotate(210)"/>
      <line x1="0" y1="-22" x2="0" y2="-35" transform="rotate(240)"/>
      <line x1="0" y1="-22" x2="0" y2="-35" transform="rotate(270)"/>
      <line x1="0" y1="-22" x2="0" y2="-35" transform="rotate(300)"/>
      <line x1="0" y1="-22" x2="0" y2="-35" transform="rotate(330)"/>
    </g>
  </svg>
</div>

<div class="abs card" role="img" aria-label="Bare trees standing in water at orange sunset" style="left:786px;top:125px;background:linear-gradient(180deg,#f08a1c 0%,#f4a526 45%,#6a3410 75%,#2a1608 100%)">
  <span class="card-label">Some Goes wallpaper name here</span>
  <span class="dl"><svg width="11" height="11" fill="none" stroke="#fff" stroke-width="1.3"><path d="M5.5 1v6M3 5l2.5 2.5L8 5M1 8v2h9V8"/></svg></span>
</div>

<div class="abs card" role="img" aria-label="Glass sphere reflecting a lake sunset" style="left:387px;top:399px;background:linear-gradient(180deg,#3f6fd8 0%,#e8743a 45%,#f4a23a 55%,#3a2a6a 80%,#1c1736 100%)">
  <span class="card-label">Some Goes wallpaper name here</span>
  <span class="dl"><svg width="11" height="11" fill="none" stroke="#fff" stroke-width="1.3"><path d="M5.5 1v6M3 5l2.5 2.5L8 5M1 8v2h9V8"/></svg></span>
</div>

<div class="abs card" role="img" aria-label="Blue and magenta starry nebula" style="left:786px;top:399px;background:linear-gradient(160deg,#0d1d3e 0%,#1a6fa8 30%,#0e1640 55%,#7a2ca0 75%,#101433 100%)">
  <span class="card-label">Some Goes wallpaper name here</span>
  <span class="dl"><svg width="11" height="11" fill="none" stroke="#fff" stroke-width="1.3"><path d="M5.5 1v6M3 5l2.5 2.5L8 5M1 8v2h9V8"/></svg></span>
</div>

<div class="abs card" role="img" aria-label="Palm trees under a blue cloudy sky" style="left:387px;top:675px;height:92px;background:linear-gradient(180deg,#2e7fc4,#6fb3df 60%,#1f3a2a)"></div>
<div class="abs card" role="img" aria-label="Mountain ridge under a pink dusk sky" style="left:786px;top:675px;height:92px;background:linear-gradient(180deg,#6f7fa6,#c99aa4 55%,#8a4a48)"></div>

<div class="abs scroll-thumb"></div>

<!-- footer -->
<div class="abs footer"></div>
<div class="abs foot-gray"></div>
<svg class="abs" style="left:370px;top:783px" width="6" height="9" fill="none" stroke="#333" stroke-width="1.3"><path d="M5 1L1.5 4.5 5 8"/></svg>
<div class="abs pg pg-prev">‹ PREV</div>
<div class="abs pg" style="left:964px;width:20px">1</div>
<div class="abs pg pg-cur">2</div>
<div class="abs pg" style="left:1027px;width:20px">3</div>
<div class="abs pg" style="left:1052px;width:16px">...</div>
<div class="abs pg" style="left:1072px;width:26px">82</div>
<div class="abs pg pg-next">NEXT ›</div>

</body>
</html>
```